INTERNATIONAL SPEAKING BUSINESS FOR WOMEN NEEDS A BROCHURE DESIGN

HEARTWARD CIRCLE IS AN INTERNATIONAL FEMALE NETWORK PROVIDING ITS MEMBERS THE UK'S NUMBER ONE RELATIONSHIP SEMINAR FOR WOMEN.
WE ARE ABOUT TO GO LIVE AGAIN AFTER 18 MONTHS AND ONE OF OUR OFFERINGS AT THIS LIVE EVENT, IS OUR CONNECTION GROWTH PROGRAMME - AND THIS IS WHERE YOU COME IN :)
IM LOOKING FOR AN ELEGANT, EASY AND WARM TO THE EYE BROCHURE WHICH CAPTURES SOME OF OUR BEST TESTIMONIALS AND CLIENTS. WE HAVE THE LOGO, THE IMAGES AND THE COPY . WE JUST NEED YOUR AMAZING CREATIVE TALENT AND SKILL TO PUT IT ALL TOGETHER TO LOOK ELEGANT AND PROFESSIONAL, YET WELCOMING AND INSPIRING.
OUR IDEAL CLIENT IS A SINGLE, SUCCESSFUL, PROFESSIONAL WOMAN WANTING TO FIND A SOLUTION TO HER RELATIONSHIP CHALLENGES. SHE WANTS TO LET GO OF HER FEARS OF PAST RELATIONSHIPS AND ALIGN WITH AN AMAZING RELATIONSHIP. OUR AIM WITH THE BROCHURE IS TO SHOW THEM WHAT WE DO, HOW WE DO IT AND HOW OUR EXISTING CLIENTS HAVE ALREADY DONE THIS.
THIS IS JUST ONE OF MANY CREATIVE WORKS NEEDED TO BE CARRIED OUT OVER THESE NEXT FEW WEEKS
SO WE ARE LOOKING FOR OUR IDEAL CREATIVE PARTNER ! HOPING TO FIND YOU HERE ;)
heartwardcircle-example.com
professional, successful women between 30 and 65 looking to resolve their relationship problems
Speaking Business/ Seminars / webinars/ Relationships Coaching for Women
- Similar to logo and website heartwardcircle-example.com

```html
<!DOCTYPE html>
<html lang="en">
<head>
<meta charset="utf-8">
<title>Heartward Circle – Trifold Brochure</title>
<link href="https://fonts.googleapis.com/css2?family=Montserrat:wght@400;600;700&family=Open+Sans:wght@400;600&display=swap" rel="stylesheet">
<style>
:root{
  --pink:#d41f4e;
  --pink-deep:#b5123a;
  --pink-soft:#e8557a;
  --silver:#c9c9cc;
  --ink:#4a4a4f;
  --paper:#ffffff;
  --stage:#e9e9eb;
  --photo-a:#c9c3c1;
  --photo-b:#8f8786;
}
*{box-sizing:border-box;margin:0;padding:0}
html,body{width:702px;height:1200px;overflow:hidden;background:var(--stage)}
body{position:relative;font-family:"Open Sans",Arial,sans-serif;color:var(--ink)}
.spread{position:absolute;left:21px;width:660px;height:450px;background:var(--paper);overflow:hidden;box-shadow:0 2px 8px rgba(0,0,0,.12)}
.spread--outside{top:110px}
.spread--inside{top:640px}
.spread__waves{position:absolute;left:0;top:0;width:660px;height:450px}
.spread__waves--front{z-index:2;pointer-events:none}
.panel{position:absolute;top:0;width:220px;height:450px;padding:16px 16px}
.panel--1{left:0}.panel--2{left:220px}.panel--3{left:440px}
.fold{position:absolute;top:0;width:1px;height:450px;background:rgba(0,0,0,.06);z-index:3}
.copy{font-size:5.6px;line-height:1.55;margin-bottom:7px}
.heading{font-family:"Montserrat",Arial,sans-serif;font-weight:700;font-size:6.6px;color:var(--pink);letter-spacing:.3px;margin-bottom:4px;text-transform:uppercase}
.bullets{list-style:none;margin-bottom:8px}
.bullets li{font-size:5.6px;line-height:1.55;padding-left:8px;position:relative;margin-bottom:3px}
.bullets li::before{content:"";position:absolute;left:0;top:3px;width:3px;height:3px;border-radius:50%;background:var(--pink)}
.photo{position:absolute;background:linear-gradient(160deg,var(--photo-a),var(--photo-b))}
.photo--pink{background:linear-gradient(160deg,#e58aa2,var(--pink-deep))}
.photo--light{background:linear-gradient(160deg,#f1e4e1,#cdb7b3)}
.brand{display:flex;align-items:center;gap:5px;font-family:"Montserrat",Arial,sans-serif;font-weight:700;color:var(--pink);text-transform:uppercase}
.brand__dot{width:10px;height:10px;border-radius:50%;background:var(--pink);flex:none}
.brand--center{position:absolute;left:0;right:0;top:80px;flex-direction:column;font-size:9px;letter-spacing:.6px}
.brand--center .brand__dot{width:34px;height:34px;margin-bottom:6px}
.brand--corner{position:absolute;left:22px;top:20px;font-size:7.5px}
.contact{position:absolute;left:82px;top:176px}
.contact__name{font-family:"Montserrat",Arial,sans-serif;font-size:10px;color:var(--pink);letter-spacing:.6px}
.contact__role{font-size:5.6px;margin-bottom:5px}
.contact__row{display:flex;align-items:center;gap:4px;font-size:5.4px;margin-bottom:3px}
.contact__row svg{width:6px;height:6px;fill:var(--pink);flex:none}
.cover__title{position:absolute;left:22px;top:44px;font-family:"Montserrat",Arial,sans-serif;font-weight:700;font-size:10px;color:var(--pink);line-height:1.2}
.cover__sub{position:absolute;left:22px;top:62px;font-size:6px;line-height:1.4;width:176px}
.cover__tagline{position:absolute;left:22px;top:334px;width:120px;font-family:"Montserrat",Arial,sans-serif;font-size:7.5px;line-height:1.45;color:var(--paper);z-index:3}
.portrait{position:absolute;left:72px;top:296px;width:76px;height:76px;border-radius:50%;border:3px solid var(--paper);background:linear-gradient(160deg,#6a5350,#2d2425);z-index:3}
.stack{position:absolute;left:16px;right:16px}
</style>
</head>
<body>

<section class="spread spread--outside" aria-label="Brochure outside spread">
  <svg class="spread__waves" viewBox="0 0 660 450" aria-hidden="true">
    <rect x="0" y="0" width="220" height="8" fill="var(--pink)"/>
  </svg>

  <div class="panel panel--1">
    <p class="copy" style="margin-top:10px">Heartward Circle is an international network of women who want calm, lasting love. Our seminars guide you through the patterns that hold you back and help you build the relationship you deserve.</p>
    <p class="heading">What you will gain</p>
    <ul class="bullets">
      <li>Clear insight into the beliefs that shaped your past relationships.</li>
      <li>Practical tools to open your heart with confidence.</li>
    </ul>
    <p class="heading">About the seminar</p>
    <p class="copy">Two immersive days of teaching, reflection and honest conversation with women who share your goals.</p>
    <p class="heading">Is this programme for you?</p>
    <p class="copy">If you are successful at work yet feel stuck in love, this programme gives you the space to let go of old fears.</p>
    <div class="photo" role="img" aria-label="Photo of a woman speaking at a seminar" style="left:0;top:300px;width:220px;height:150px"></div>
  </div>

  <div class="panel panel--2">
    <div class="brand brand--center"><span class="brand__dot"></span>Heartward Circle</div>
    <div class="contact">
      <p class="contact__name">MARA ELLISON</p>
      <p class="contact__role">Manager</p>
      <p class="contact__row"><svg viewBox="0 0 10 10"><path d="M2 0h2l1 3-1.5 1a6 6 0 0 0 2.5 2.5L7 5l3 1v2a2 2 0 0 1-2 2A8 8 0 0 1 0 2a2 2 0 0 1 2-2z"/></svg>+44 0000 000 111</p>
      <p class="contact__row"><svg viewBox="0 0 10 10"><path d="M0 2h10v6H0z M0 2l5 3 5-3" /></svg>hello@heartwardcircle-example.com</p>
      <p class="contact__row"><svg viewBox="0 0 10 10"><circle cx="5" cy="5" r="4.5"/></svg>heartwardcircle-example.com</p>
    </div>
    <div class="portrait" role="img" aria-label="Portrait photo of the programme manager"></div>
  </div>

  <div class="panel panel--3">
    <div class="brand brand--corner"><span class="brand__dot"></span>Heartward Circle</div>
    <p class="cover__title">HEARTWARD CIRCLE</p>
    <p class="cover__sub">Let go of the past,<br>align with a lasting relationship</p>
    <div class="photo photo--light" role="img" aria-label="Photo of a smiling woman with glasses" style="left:0;top:92px;width:220px;height:190px"></div>
    <p class="cover__tagline">The UK's number one relationship seminar for women</p>
  </div>

  <svg class="spread__waves spread__waves--front" viewBox="0 0 660 450" aria-hidden="true">
    <path d="M0 300 C60 280 140 300 220 285 L220 450 L0 450Z" fill="var(--pink)" opacity=".55"/>
    <path d="M220 270 C280 240 360 300 440 260 L440 450 L220 450Z" fill="var(--pink)"/>
    <path d="M440 270 C500 300 590 250 660 262 L660 450 L440 450Z" fill="var(--pink)"/>
    <path d="M0 292 C60 272 140 292 220 277 C280 232 360 292 440 252 C500 292 590 242 660 254" fill="none" stroke="var(--silver)" stroke-width="4"/>
  </svg>
  <span class="fold" style="left:220px"></span><span class="fold" style="left:440px"></span>
</section>

<section class="spread spread--inside" aria-label="Brochure inside spread">
  <div class="panel panel--1">
    <div class="photo photo--light" role="img" aria-label="Photo of a smiling woman" style="left:0;top:0;width:220px;height:120px"></div>
    <div class="stack" style="top:130px">
      <p class="heading">Connection Growth Programme</p>
      <p class="copy">A year-long journey for women ready to transform how they love. Monthly sessions, coaching calls and a warm community keep you supported every step.</p>
      <p class="heading">Who it is for</p>
      <p class="copy">Single professional women aged 30 to 65 who are ready to release old hurt and welcome a healthy partnership.</p>
      <p class="heading">How it works</p>
      <p class="copy">Live workshops, guided exercises and one-to-one reviews help you turn insight into lasting change.</p>
    </div>
  </div>

  <div class="panel panel--2">
    <div class="stack" style="top:22px">
      <p class="heading">What our members say</p>
      <p class="copy">"I came in guarded and left feeling lighter than I have in years. Within six months I met someone who truly sees me."</p>
      <p class="copy">"The tools are simple and practical. I finally understand why I kept choosing the same kind of partner."</p>
      <p class="heading">Our approach</p>
      <p class="copy">We blend coaching, psychology and real stories so each woman can find her own path to love with clarity and kindness.</p>
      <p class="heading">Your next step</p>
      <p class="copy">Join us at the live event and reserve your place in the programme before spaces close.</p>
    </div>
    <div class="photo photo--pink" role="img" aria-label="Photo of seminar attendees in a pink-lit hall" style="left:0;top:300px;width:220px;height:150px"></div>
  </div>

  <div class="panel panel--3">
    <div class="stack" style="top:22px">
      <p class="heading">Real results</p>
      <p class="copy">Thousands of women have attended our seminars across the UK and beyond, and many now share their lives with loving partners.</p>
      <p class="heading">Stories of change</p>
      <p class="copy">"I stopped chasing and started choosing. The circle gave me the courage to trust again."</p>
      <p class="copy">"Warm, wise and honest. Every session felt like coming home."</p>
    </div>
    <div class="photo" role="img" aria-label="Photo of women embracing at an event" style="left:30px;top:220px;width:170px;height:110px"></div>
  </div>

  <svg class="spread__waves spread__waves--front" viewBox="0 0 660 450" aria-hidden="true">
    <path d="M0 370 C70 345 150 385 220 360 L220 450 L0 450Z" fill="var(--pink)"/>
    <path d="M220 360 C300 330 370 390 440 350 L440 450 L220 450Z" fill="var(--pink)" opacity=".6"/>
    <path d="M440 350 C520 380 600 330 660 345 L660 450 L440 450Z" fill="var(--pink)"/>
    <path d="M0 362 C70 337 150 377 220 352 C300 322 370 382 440 342 C520 372 600 322 660 337" fill="none" stroke="var(--silver)" stroke-width="4"/>
  </svg>
  <span class="fold" style="left:220px"></span><span class="fold" style="left:440px"></span>
</section>

</body>
</html>
```